Business Card Design

I used to run a Mountaineering school and am getting back into business and just want a generic type card with an adventure theme. Core activities will be mountaineering, rock climbing, canyoning, expeditions, cross country skiing,

Industry/Entity Type

School

Contact Information for Business Card

Colin Ashby Adventure Guide
email: tallpinecolin@mailvane.net
+61472 836 915.

```html
<!DOCTYPE html>
<html lang="en">
<head>
<meta charset="utf-8">
<title>Colin Ashby – Adventure Guide</title>
<link rel="stylesheet" href="https://fonts.googleapis.com/css2?family=Arimo:wght@700&family=Audiowide&family=Russo+One&display=swap">
<style>
  :root {
    --magenta: #ff10f0;
    --sky: #33b8f5;
    --ink: #0a0a0a;
    --paper: #ffffff;
    --carabiner: #9a9a9a;
  }
  html, body {
    margin: 0;
    padding: 0;
    width: 1000px;
    height: 1200px;
    overflow: hidden;
    background: var(--paper);
  }
  .canvas {
    position: relative;
    width: 1000px;
    height: 1200px;
  }
  .card-art {
    position: absolute;
    inset: 0;
  }
  .name {
    font-family: "Russo One", sans-serif;
    font-size: 62px;
    fill: var(--ink);
    stroke: var(--paper);
    stroke-width: 3px;
    paint-order: stroke;
  }
  .role {
    font-family: "Audiowide", sans-serif;
    font-size: 52px;
    fill: var(--sky);
    stroke: var(--magenta);
    stroke-width: 2.5px;
    paint-order: stroke;
  }
  .contact {
    font-family: "Arimo", sans-serif;
    font-weight: 700;
    font-size: 27px;
    fill: var(--ink);
  }
</style>
</head>
<body>
<main class="canvas">
  <svg class="card-art" width="1000" height="1200" viewBox="0 0 1000 1200" xmlns="http://www.w3.org/2000/svg">
    <!-- card frame -->
    <rect class="card-frame" x="65" y="370" width="861" height="352" rx="22" ry="22"
          fill="var(--paper)" stroke="var(--magenta)" stroke-width="7"/>

    <!-- name band -->
    <path class="name-band" d="M178 486 L900 484 Q918 484 908 500 L866 552 Q860 558 850 558 L170 558 Z"
          fill="var(--magenta)"/>

    <!-- carabiner artwork placeholder -->
    <path class="carabiner" role="img" aria-label="Climbing carabiner illustration forming the first letter"
          d="M150 405 Q240 392 258 430 Q266 455 240 480 L170 552 Q150 570 120 560 Q88 548 92 515 Q100 460 150 405 Z"
          fill="var(--carabiner)" stroke="var(--magenta)" stroke-width="8"/>

    <!-- name -->
    <text class="name" x="200" y="549" textLength="700" lengthAdjust="spacingAndGlyphs"
          transform="skewX(-14) translate(136 0)">COLIN ASHBY</text>

    <!-- role -->
    <text class="role" x="166" y="610" textLength="702" lengthAdjust="spacingAndGlyphs">ADVENTURE GUIDE</text>

    <!-- contact details -->
    <text class="contact contact-phone" x="100" y="647" textLength="196" lengthAdjust="spacingAndGlyphs">+61472 836 915</text>
    <text class="contact contact-email" x="362" y="647" textLength="523" lengthAdjust="spacingAndGlyphs">tallpinecolin@mailvane.net</text>
  </svg>
</main>
</body>
</html>
```